Hello my name is Colin, I am Starting a business called Harbor Health and fitness and am in need of a memorable business card.
It is a personal training studio. I have added the logo that i would like to be on the left center om my business card. i would like room left up the top for a heading sentence such as. "Is your body shocking for all the wrong reasons". there must be room left on the right of the logo below the main heading for 3 sub headings.
then under those 3 headings and logo room for another larger heading eg. "give me a call and learn how to eat chocolate, drink bear and have great sex". in what room is left i would like to be used for my contact details, use I'm Colin Pettersby your fitness expert on the left then on the right Phone, Email and website space in at least 12 Point. Very specific i know :) now onto the back, for the back i would like an eye catching graphic and room for one main headline and 3 bullet points centered just write anything i will choose what to put in them when i pick a winner. Thank you very much for sticking through all of that :) i appreciate you taking the time to read it and hopefully undergo designing me a business card.
I can't wait to see the designs!

Target Market(s)

slightly more towards females although it would probably be best if it was targeted towards both sexes

Industry/Entity Type

Training

Requirements
Nice to have
• I would love to see if anyone could come up with a design that would really make my card stand out and be memorable.
Should not have
• tacky fitness photos of abs and muscles etc.

```html
<!DOCTYPE html>
<html lang="en">
<head>
<meta charset="utf-8">
<title>Harbor Health and Fitness – Business Card</title>
<link href="https://fonts.googleapis.com/css2?family=Tinos:wght@400&display=swap" rel="stylesheet">
<style>
  :root {
    --navy: #1c3f6e;
    --navy-light: #2a4d7f;
    --marker: #4f7db6;
    --paper: #f5f5f5;
    --paper-edge: #e0e0e0;
    --ink: #1c3f6e;
    --white: #ffffff;
    --backdrop: #dcdcdc;
  }
  html, body {
    margin: 0;
    padding: 0;
    width: 1120px;
    height: 1200px;
    overflow: hidden;
    background: var(--backdrop);
    font-family: "Tinos", "Times New Roman", serif;
  }
  .canvas { position: relative; width: 1120px; height: 1200px; }

  .card {
    position: absolute;
    left: 201px;
    width: 719px;
    height: 414px;
    overflow: hidden;
    box-shadow: 0 6px 14px rgba(0,0,0,0.25);
  }
  .card-front {
    top: 105px;
    background: radial-gradient(ellipse at 45% 45%, var(--paper) 0%, #ececec 60%, var(--paper-edge) 100%);
  }
  .card-back {
    top: 651px;
    background: radial-gradient(ellipse at 60% 30%, var(--navy-light) 0%, var(--navy) 70%);
  }

  .brand {
    position: absolute;
    left: 29px;
    top: 38px;
    display: flex;
    align-items: center;
    gap: 8px;
    color: var(--ink);
    font-size: 24px;
    line-height: 1;
  }
  .brand-mark { width: 12px; height: 12px; background: var(--ink); }

  .side-tab {
    position: absolute;
    left: 0;
    top: 106px;
    width: 12px;
    height: 201px;
    background: var(--navy);
  }

  .message-panel {
    position: absolute;
    left: 360px;
    top: 106px;
    width: 359px;
    height: 201px;
    background: var(--navy);
    box-shadow: -2px 2px 6px rgba(0,0,0,0.3);
  }
  .marker {
    position: absolute;
    left: 350px;
    width: 26px;
    height: 26px;
  }
  .marker-one { top: 133px; }
  .marker-two { top: 233px; }

  .headline, .sub-list li, .call-to-action, .contact, .intro {
    position: absolute;
    margin: 0;
    white-space: nowrap;
  }
  .headline { font-size: 16px; color: var(--white); }
  .sub-list {
    position: absolute;
    margin: 0;
    padding: 0;
    list-style: none;
  }
  .sub-list li {
    position: relative;
    padding-left: 18px;
    font-size: 12.5px;
    line-height: 19px;
    color: var(--white);
  }
  .sub-list li::before {
    content: "";
    position: absolute;
    left: 0;
    top: 9px;
    width: 10px;
    height: 3px;
    background: var(--white);
  }

  .front-headline { left: 389px; top: 136px; }
  .front-subs { left: 390px; top: 157px; }
  .call-to-action {
    left: 389px;
    top: 235px;
    font-size: 16px;
    line-height: 22px;
    color: var(--white);
  }

  .intro { left: 29px; top: 366px; font-size: 16px; color: var(--ink); }
  .contact { top: 387px; font-size: 16px; color: var(--ink); }
  .contact .dot {
    display: inline-block;
    width: 9px;
    height: 9px;
    background: var(--ink);
    margin: 0 7px 1px 6px;
  }
  .contact-phone { left: 29px; }
  .contact-web { left: 246px; }
  .contact-email { left: 487px; }

  .graphic-area {
    position: absolute;
    left: 57px;
    top: 96px;
    width: 224px;
    height: 222px;
    border-radius: 6px;
    background: linear-gradient(135deg, rgba(255,255,255,0.16), rgba(255,255,255,0.08));
  }
  .back-headline { left: 363px; top: 168px; }
  .back-subs { left: 364px; top: 189px; }
</style>
</head>
<body>
<div class="canvas">

  <section class="card card-front">
    <div class="brand"><span class="brand-mark"></span><span class="brand-name">Harbor Health and Fitness</span></div>

    <div class="side-tab"></div>
    <div class="message-panel"></div>

    <svg class="marker marker-one" viewBox="0 0 26 26" aria-hidden="true">
      <polygon points="0,13 10,2 26,2 26,24 10,24" fill="var(--marker)"/>
    </svg>
    <svg class="marker marker-two" viewBox="0 0 26 26" aria-hidden="true">
      <polygon points="0,13 10,2 26,2 26,24 10,24" fill="var(--marker)"/>
    </svg>

    <p class="headline front-headline">Is your body shocking for all the wrong reasons</p>
    <ul class="sub-list front-subs">
      <li>Is your body shocking for all the wrong reasons</li>
      <li>Is your body shocking for all the wrong reasons</li>
      <li>Is your body shocking for all the wrong reasons</li>
    </ul>
    <p class="call-to-action">give me a call and learn how to eat chocolate,<br>drink bear and have great sex</p>

    <p class="intro">I'm Colin Pettersby your fitness expert</p>
    <p class="contact contact-phone">Phone<span class="dot"></span>01234567890</p>
    <p class="contact contact-web">Web<span class="dot"></span>www.yourwebsite.com</p>
    <p class="contact contact-email">Email<span class="dot"></span>yourname@email.com</p>
  </section>

  <section class="card card-back">
    <div class="graphic-area" role="img" aria-label="Grid of nine white fitness pictograms: running, stretching, swimming, rowing, dancing, yoga, ball exercise, healthy apple and weight lifting"></div>

    <p class="headline back-headline">Is your body shocking for all the wrong reasons</p>
    <ul class="sub-list back-subs">
      <li>Is your body shocking for all the wrong reasons</li>
      <li>Is your body shocking for all the wrong reasons</li>
      <li>Is your body shocking for all the wrong reasons</li>
    </ul>
  </section>

</div>
</body>
</html>
```